RK Website Home Page Design

The task is to develop a winning design for a replacement website for our client RK Plumbing, Heating, AC & Remodeling. ct

```html
<!DOCTYPE html>
<html lang="en">
<head>
<meta charset="utf-8">
<title>RK Plumbing, Heating, AC &amp; Remodeling</title>
<link href="https://fonts.googleapis.com/css2?family=Poppins:wght@400;500;600;700;800&display=swap" rel="stylesheet">
<style>
:root{
  --navy:#1d3461;
  --navy-dark:#1a2f58;
  --yellow:#ffe600;
  --amber:#fcc200;
  --grey-bg:#f4f4f4;
  --hex:#ececec;
  --text:#222;
  --muted:#555;
  --white:#fff;
}
*{box-sizing:border-box;margin:0;padding:0}
html,body{width:1200px;height:5263px;overflow:hidden}
body{font-family:'Poppins',sans-serif;color:var(--text);background:var(--white);position:relative}
section,header,footer,nav{position:absolute;left:0;width:1200px}
.abs{position:absolute}
.btn{position:absolute;display:flex;align-items:center;justify-content:center;background:var(--yellow);color:var(--navy);font-weight:500;text-decoration:none}
.section-title{position:absolute;left:0;width:1200px;text-align:center;color:var(--navy);font-weight:700;font-size:29px;letter-spacing:.2px}

/* header */
.site-header{top:0;height:155px;background:var(--white)}
.brand{position:absolute;left:86px;top:40px;display:flex;align-items:center;gap:12px}
.brand-dot{width:38px;height:38px;border-radius:50%;background:var(--yellow)}
.brand-name{font-weight:800;font-size:26px;color:var(--navy);line-height:1}
.topbar{position:absolute;left:368px;top:0;width:832px;height:58px;background:#f1f1f1;clip-path:polygon(0 0,100% 0,100% 100%,6% 100%);display:flex;justify-content:flex-end;align-items:center;gap:26px;padding-right:86px;font-size:14px;color:#333}
.topbar span{display:flex;align-items:center;gap:8px}
.hdr-btn{top:80px;height:47px;border-radius:24px;font-size:15px}

.main-nav{top:155px;height:55px;background:var(--navy);display:flex;align-items:stretch;padding-left:82px}
.main-nav a{color:var(--white);font-size:13px;text-decoration:none;display:flex;align-items:center;padding:0 11px}
.main-nav a.active{background:var(--yellow);color:var(--navy)}

/* hero */
.hero{top:210px;height:608px}
.hero-photo{position:absolute;inset:0;background:linear-gradient(100deg,#eef0f1 0%,#e3e6e8 45%,#c9ced2 70%,#e9ecee 100%)}
.hero-title{position:absolute;left:249px;top:152px;font-size:52px;line-height:60px;font-weight:800;color:var(--navy)}
.hero-btn{left:253px;top:360px;width:391px;height:82px;border:3px solid var(--white);border-radius:6px;font-size:19px;font-weight:600}
.dots{position:absolute;display:flex;gap:5px}
.dots i{width:14px;height:14px;border-radius:50%;background:#b8c0c9;display:block}
.dots i.on{background:var(--navy)}
.hero .dots i{background:rgba(255,255,255,.6)}
.hero .dots i.on{background:var(--white)}

/* services */
.services{top:818px;height:813px}
.service{position:absolute;width:240px;text-align:center}
.service svg{display:block;margin:0 auto}
.service p{font-size:20px;color:#222;margin-top:8px;line-height:26px}
.service.active p{color:var(--navy)}

/* request */
.request{top:1631px;height:863px;background:var(--grey-bg)}
.field{position:absolute;background:var(--white);border:1px solid #ebebeb;font-size:14px;color:#555;padding:15px 24px;font-family:inherit}
.submit{left:499px;top:707px;width:202px;height:72px;font-size:18px;font-weight:600;border:none}

/* reminder */
.reminder{top:2494px;height:531px}
.reminder h2{position:absolute;left:84px;top:136px;font-size:29px;font-weight:700;color:var(--navy)}
.reminder p{position:absolute;left:84px;top:198px;width:440px;font-size:14.5px;line-height:31px;color:#333}
.reminder-photo{position:absolute;left:638px;top:90px;width:445px;height:304px;border-radius:20px;background:linear-gradient(120deg,#f4f4f4,#dcdcdc 60%,#cfc8c0)}

/* difference */
.difference{top:3025px;height:542px;background:var(--grey-bg)}
.photo-a{position:absolute;left:86px;top:63px;width:394px;height:295px;border-radius:16px;background:linear-gradient(135deg,#8e949a,#c9ccce 55%,#6f757b)}
.photo-b{position:absolute;left:269px;top:245px;width:280px;height:230px;border-radius:16px;border:4px solid var(--white);background:linear-gradient(180deg,#dedede,#b9bcbf 55%,#e8e8e8)}
.difference h2{position:absolute;left:601px;top:90px;font-size:29px;font-weight:700;color:var(--navy)}
.difference p{position:absolute;left:601px;top:156px;width:505px;font-size:14px;line-height:31px;color:#333}
.learn{left:601px;top:376px;width:161px;height:64px;border-radius:10px;font-size:17px}

/* savings */
.savings{top:3567px;height:628px}
.savings .section-title{top:98px;line-height:38px}
.offer{position:absolute;top:259px;width:325px;height:242px;background:var(--navy);border-radius:12px;text-align:center;color:var(--white)}
.offer h3{font-weight:400;font-size:25px;margin-top:56px}
.offer .amt{color:var(--yellow);font-weight:700;font-size:31px;margin-top:4px}
.offer .desc{font-size:14px;line-height:24px;margin-top:6px}
.offer .details{left:98px;top:228px;width:128px;height:30px;border-radius:4px;font-size:11px;font-weight:600}

/* blog */
.blog{top:4195px;height:719px;background:var(--grey-bg)}
.blog .section-title{top:108px}
.post{position:absolute;top:212px;width:315px;height:386px;background:var(--white)}
.post-photo{height:194px}
.post .date{font-size:12px;color:#333;margin:22px 0 0 20px}
.post h3{font-size:19px;font-weight:600;color:var(--navy);margin:2px 0 0 20px}
.post p{font-size:15px;line-height:21px;color:#555;margin:4px 20px 0;text-align:justify}
.readmore{left:194px;top:339px;width:121px;height:25px;background:var(--amber);color:var(--white);font-size:12px;font-weight:600}

/* footer */
.site-footer{top:4914px;height:349px;background:var(--navy);color:var(--white)}
.f-brand{position:absolute;left:94px;top:136px;display:flex;align-items:center;gap:12px}
.f-brand .brand-name{color:var(--white)}
.social{position:absolute;left:302px;top:212px;width:28px;height:28px;border-radius:50%;background:#c7cfda}
.f-head{position:absolute;top:100px;font-size:14px;font-weight:600;color:var(--yellow)}
.f-list{position:absolute;top:130px;list-style:none;font-size:14px;line-height:20px}
.f-list li::before{content:"";display:inline-block;width:5px;height:5px;border-radius:50%;background:var(--white);margin-right:12px;vertical-align:middle}
.contact-line{position:absolute;left:899px;display:flex;gap:10px;font-size:14px;line-height:19px}
.f-rule{position:absolute;left:86px;top:274px;width:1028px;height:1px;background:rgba(255,255,255,.35)}
.copy{position:absolute;left:86px;top:302px;font-size:13px}
.cards{position:absolute;left:973px;top:302px;display:flex;gap:6px}
.cards i{display:block;width:31px;height:19px;background:#e7ecf3;border-radius:2px}
.cards i:nth-child(2){background:#f1b35a}
.cards i:nth-child(3){background:#4e8ed0}
</style>
</head>
<body>

<header class="site-header">
  <div class="brand"><span class="brand-dot"></span><span class="brand-name">RK PLUMBING</span></div>
  <div class="topbar">
    <span><svg width="12" height="16" viewBox="0 0 12 16"><path d="M6 0a6 6 0 0 0-6 6c0 4.5 6 10 6 10s6-5.5 6-10a6 6 0 0 0-6-6zm0 8.5A2.5 2.5 0 1 1 6 3.5a2.5 2.5 0 0 1 0 5z" fill="#1d3461"/></svg>Serving Northfield, MA &amp; Neighboring Communities</span>
    <span><svg width="15" height="15" viewBox="0 0 24 24"><path d="M6.6 10.8a15 15 0 0 0 6.6 6.6l2.2-2.2a1 1 0 0 1 1-.25 11.4 11.4 0 0 0 3.6.57 1 1 0 0 1 1 1V20a1 1 0 0 1-1 1A17 17 0 0 1 3 4a1 1 0 0 1 1-1h3.5a1 1 0 0 1 1 1c0 1.25.2 2.45.57 3.57a1 1 0 0 1-.25 1z" fill="#1d3461"/></svg>555.201.4830, 800.555.0187</span>
  </div>
  <a class="btn hdr-btn" style="left:720px;width:190px">Request Service</a>
  <a class="btn hdr-btn" style="left:922px;width:192px">Request a Quote</a>
</header>

<nav class="main-nav">
  <a>About</a><a>Plumbing</a><a class="active">Water Heaters</a><a>Heating</a><a>Air Conditioning</a><a>Indoor Air Quality</a><a>Commercial</a><a>Handy Work &amp; Remodeling</a><a>Contact</a>
</nav>

<section class="hero">
  <div class="hero-photo" role="img" aria-label="Bright bathroom with a chrome shower faucet running water into a tub"></div>
  <h1 class="hero-title">ENJOY THE BEST<br>OF HOME LIVING<br>INDOORS &amp; OUT</h1>
  <a class="btn hero-btn">Contact Us to Get Started</a>
  <div class="dots" style="left:563px;top:512px"><i class="on"></i><i></i><i></i><i></i></div>
</section>

<section class="services">
  <h2 class="section-title" style="top:110px">MORE OF WHAT YOU NEED</h2>
  <div class="service active" style="left:115px;top:219px">
    <svg width="153" height="174" viewBox="0 0 153 174"><polygon points="76.5,0 153,43.5 153,130.5 76.5,174 0,130.5 0,43.5" fill="#ececec"/><circle cx="76.5" cy="87" r="55" fill="#1d3461"/><path d="M62 78h22v-6h-6v-4h12v4h-2v6h6a6 6 0 0 1 6 6v6h-8v-4H62z" fill="#ffe600"/><path d="M94 96c0 3-2 5-2 5s-2-2-2-5 2-5 2-5 2 2 2 5z" fill="#ffe600"/></svg>
    <p>Plumbing</p>
  </div>
  <div class="service" style="left:360px;top:219px">
    <svg width="153" height="174" viewBox="0 0 153 174"><polygon points="76.5,0 153,43.5 153,130.5 76.5,174 0,130.5 0,43.5" fill="#ececec"/><circle cx="76.5" cy="87" r="55" fill="#fff"/><path d="M70 68c6 8 10 13 10 19a10 10 0 0 1-20 0c0-6 4-11 10-19z" fill="#1d3461"/><path d="M84 80c4 6 8 9 8 14a6 6 0 0 1-12 0c0-5 2-8 4-14z" fill="#1d3461"/></svg>
    <p>Water Heaters</p>
  </div>
  <div class="service" style="left:603px;top:219px">
    <svg width="153" height="174" viewBox="0 0 153 174"><polygon points="76.5,0 153,43.5 153,130.5 76.5,174 0,130.5 0,43.5" fill="#ececec"/><circle cx="76.5" cy="87" r="55" fill="#fff"/><path d="M77 66c10 10 11 18 8 24a9 9 0 0 1-16 0c-2-5 2-9 4-10 0 4 2 6 4 6 3-5 2-12 0-20z" fill="#1d3461"/><rect x="66" y="102" width="22" height="3" fill="#1d3461"/></svg>
    <p>Heating</p>
  </div>
  <div class="service" style="left:841px;top:219px">
    <svg width="153" height="174" viewBox="0 0 153 174"><polygon points="76.5,0 153,43.5 153,130.5 76.5,174 0,130.5 0,43.5" fill="#ececec"/><circle cx="76.5" cy="87" r="55" fill="#fff"/><g stroke="#1d3461" stroke-width="3" stroke-linecap="round"><line x1="76.5" y1="69" x2="76.5" y2="105"/><line x1="61" y1="78" x2="92" y2="96"/><line x1="61" y1="96" x2="92" y2="78"/><path d="M71 72l5.5 4 5.5-4M71 102l5.5-4 5.5 4" fill="none"/></g></svg>
    <p>Air Conditioning</p>
  </div>
  <div class="service" style="left:115px;top:500px">
    <svg width="153" height="174" viewBox="0 0 153 174"><polygon points="76.5,0 153,43.5 153,130.5 76.5,174 0,130.5 0,43.5" fill="#ececec"/><circle cx="76.5" cy="87" r="55" fill="#fff"/><rect x="63" y="73" width="28" height="28" fill="none" stroke="#1d3461" stroke-width="3"/><path d="M69 86l7 7 16-18" fill="none" stroke="#1d3461" stroke-width="4"/></svg>
    <p>Indoor Air Quality</p>
  </div>
  <div class="service" style="left:360px;top:500px">
    <svg width="153" height="174" viewBox="0 0 153 174"><polygon points="76.5,0 153,43.5 153,130.5 76.5,174 0,130.5 0,43.5" fill="#ececec"/><circle cx="76.5" cy="87" r="55" fill="#fff"/><path d="M76.5 66c6 8 9 12 9 17a9 9 0 0 1-18 0c0-5 3-9 9-17z" fill="#1d3461"/><g fill="#1d3461"><circle cx="66" cy="99" r="1.5"/><circle cx="71" cy="99" r="1.5"/><circle cx="76.5" cy="99" r="1.5"/><circle cx="82" cy="99" r="1.5"/><circle cx="87" cy="99" r="1.5"/><circle cx="71" cy="104" r="1.5"/><circle cx="76.5" cy="104" r="1.5"/><circle cx="82" cy="104" r="1.5"/></g></svg>
    <p>Water Filtration</p>
  </div>
  <div class="service" style="left:603px;top:500px">
    <svg width="153" height="174" viewBox="0 0 153 174"><polygon points="76.5,0 153,43.5 153,130.5 76.5,174 0,130.5 0,43.5" fill="#ececec"/><circle cx="76.5" cy="87" r="55" fill="#fff"/><path d="M64 84a13 13 0 0 1 22-8M89 90a13 13 0 0 1-22 8" fill="none" stroke="#1d3461" stroke-width="4"/><path d="M86 68v9h-9M67 106v-9h9" fill="none" stroke="#1d3461" stroke-width="4"/></svg>
    <p>Remodeling &amp;<br>Handy Work</p>
  </div>
  <div class="service" style="left:841px;top:500px">
    <svg width="153" height="174" viewBox="0 0 153 174"><polygon points="76.5,0 153,43.5 153,130.5 76.5,174 0,130.5 0,43.5" fill="#ececec"/><circle cx="76.5" cy="87" r="55" fill="#fff"/><path d="M78 66c8 10 9 18 6 25a8 8 0 0 1-14 0c-2-5 1-10 3-12 0 4 2 6 3 6 2-5 2-12 2-19z" fill="#1d3461"/></svg>
    <p>Gas Fireplaces</p>
  </div>
</section>

<section class="request">
  <h2 class="section-title" style="top:103px">REQUEST SERVICE</h2>
  <div class="field" style="left:258px;top:207px;width:331px;height:51px">Name*</div>
  <div class="field" style="left:609px;top:207px;width:331px;height:51px">E-mail*</div>
  <div class="field" style="left:258px;top:282px;width:331px;height:51px">Address</div>
  <div class="field" style="left:609px;top:282px;width:331px;height:51px">City</div>
  <div class="field" style="left:258px;top:358px;width:331px;height:51px">Zip</div>
  <div class="field" style="left:609px;top:358px;width:331px;height:51px">Phone</div>
  <div class="field" style="left:258px;top:435px;width:682px;height:231px">Comments</div>
  <button class="btn submit">SUBMIT</button>
</section>

<section class="reminder">
  <h2>BACK TO SCHOOL REMINDER</h2>
  <p>Most families see an uptick in morning “rush hour” activity once the school year begins, and so does your water heater. Can yours keep up with the increased demand? Contact us today for a water heater check-up and free quote on a replacement system.</p>
  <div class="reminder-photo" role="img" aria-label="White tank water heater mounted on a marble bathroom wall"></div>
  <div class="dots" style="left:561px;top:465px"><i class="on"></i><i></i><i></i><i></i></div>
</section>

<section class="difference">
  <div class="photo-a" role="img" aria-label="Gloved technician servicing a boiler pump and gauge"></div>
  <div class="photo-b" role="img" aria-label="Chrome faucet pouring water"></div>
  <h2>THE RK DIFFERENCE MAKERS</h2>
  <p>RK is a favorite choice among homeowners who appreciate our extensive range of home comfort and related services. Others like us best for our 100% satisfaction guarantee, while still others enjoy the many benefits that membership in our Preferred Service Club provides. Add it all up, and there’s a lot to like about RK Plumbing, Heating, AC &amp; Remodeling.</p>
  <a class="btn learn">Learn More</a>
</section>

<section class="savings">
  <h2 class="section-title">ENJOY THE SAVINGS...<br>PLUS THE ADDED COMFORT!</h2>
  <div class="offer" style="left:86px"><h3>New Water Heater</h3><div class="amt">Save $120</div><div class="desc">...on a new water heater,<br>tank-style or tankless.</div><a class="btn details">Click for Details</a></div>
  <div class="offer" style="left:441px"><h3>HVAC System</h3><div class="amt">Save $350</div><div class="desc">...on a new heating<br>or cooling system.</div><a class="btn details">Click for Details</a></div>
  <div class="offer" style="left:791px;width:323px"><h3>First-time Customer</h3><div class="amt">Save $35</div><div class="desc">...on any service<br>we provide.</div><a class="btn details">Click for Details</a></div>
</section>

<section class="blog">
  <h2 class="section-title">LATEST BLOG</h2>
  <article class="post" style="left:86px"><div class="post-photo" role="img" aria-label="Gloved hands fitting a yellow gas pipe" style="background:linear-gradient(135deg,#4a4f55,#c9b23a 55%,#5d6166)"></div><div class="date">05 MAY 2023</div><h3>Lorem ipsum dolor</h3><p>Suspendisse sollicitudin ipsum massa, a porttitor erat facilisis quis.</p><a class="btn readmore">Read More</a></article>
  <article class="post" style="left:444px"><div class="post-photo" role="img" aria-label="Red valve wheels on industrial pipes" style="background:linear-gradient(135deg,#6d6f72,#a5453a 50%,#55585c)"></div><div class="date">05 MAY 2023</div><h3>Lorem ipsum dolor</h3><p>Suspendisse sollicitudin ipsum massa, a porttitor erat facilisis quis.</p><a class="btn readmore">Read More</a></article>
  <article class="post" style="left:799px"><div class="post-photo" role="img" aria-label="Wall-mounted air conditioner in a modern living room" style="background:linear-gradient(135deg,#9a9590,#d9d6d2 55%,#7d7670)"></div><div class="date">05 MAY 2023</div><h3>Lorem ipsum dolor</h3><p>Suspendisse sollicitudin ipsum massa, a porttitor erat facilisis quis.</p><a class="btn readmore">Read More</a></article>
</section>

<footer class="site-footer">
  <div class="f-brand"><span class="brand-dot"></span><span class="brand-name">RK PLUMBING</span></div>
  <span class="social"></span>
  <div class="f-head" style="left:409px">QUICK LINKS</div>
  <ul class="f-list" style="left:409px"><li>About</li><li>Plumbing</li><li>Water Heaters</li><li>Heating</li><li>Air Conditioning</li></ul>
  <ul class="f-list" style="left:596px"><li>Indoor Air Quality</li><li>Commercial</li><li>Handy Work &amp; Remodeling</li><li>Contact</li></ul>
  <div class="f-head" style="left:899px">CONTACT US</div>
  <div class="contact-line" style="top:128px"><svg width="12" height="16" viewBox="0 0 12 16"><path d="M6 0a6 6 0 0 0-6 6c0 4.5 6 10 6 10s6-5.5 6-10a6 6 0 0 0-6-6zm0 8.5A2.5 2.5 0 1 1 6 3.5a2.5 2.5 0 0 1 0 5z" fill="#fff"/></svg><span>118 Maple Avenue<br>Northfield, MA 01360</span></div>
  <div class="contact-line" style="top:184px"><svg width="14" height="14" viewBox="0 0 24 24"><path d="M6.6 10.8a15 15 0 0 0 6.6 6.6l2.2-2.2a1 1 0 0 1 1-.25 11.4 11.4 0 0 0 3.6.57 1 1 0 0 1 1 1V20a1 1 0 0 1-1 1A17 17 0 0 1 3 4a1 1 0 0 1 1-1h3.5a1 1 0 0 1 1 1c0 1.25.2 2.45.57 3.57a1 1 0 0 1-.25 1z" fill="#fff"/></svg><span>555.201.4830,<br>800.555.0187</span></div>
  <div class="f-rule"></div>
  <div class="copy">Copyright © 2023 All Rights Reserved By Company Name</div>
  <div class="cards"><i></i><i></i><i></i><i></i></div>
</footer>

</body>
</html>
```